Medical device box for kits used for self testing purposes. Attractive simplistic design

Looking for a design that will go on a box that offer multiple range of medical testing ranging from hormones panel to diabetes and thyroid hormones. looking for something attractive and simple to go on a box 6 x 4.5 x 1 inches. attached are some examples from competitors. and our logo that be incorporated with the design.
Picture of the boxes have been attached, pick the color you think goes best with your design.

Target Market(s)

Patients and regular consumers

Industry/Entity Type

Medical

Requirements
Nice to have
• Simple design that is eye catching

```html
<!DOCTYPE html>
<html lang="en">
<head>
<meta charset="utf-8">
<title>Medical Kits – Box Front Panel</title>
<link rel="stylesheet" href="https://fonts.googleapis.com/css2?family=Nunito:wght@400;700;800&display=swap">
<style>
  :root {
    --navy: #121a45;
    --yellow: #fcc20a;
    --orange: #fb9409;
    --sky: #6aa5c4;
    --paper: #ffffff;
    --page: #ffffff;
  }
  * { margin: 0; padding: 0; box-sizing: border-box; }
  html, body {
    width: 1008px;
    height: 1200px;
    overflow: hidden;
    background: var(--page);
    font-family: "Nunito", sans-serif;
    color: var(--navy);
  }
  .box-front {
    position: absolute;
    left: 54px;
    top: 262px;
    width: 900px;
    height: 676px;
    background: var(--paper);
    box-shadow: 0 4px 18px rgba(18, 26, 69, 0.10);
  }
  .product-title {
    position: absolute;
    left: 66px;
    top: 60px;
    font-size: 64px;
    font-weight: 800;
    letter-spacing: 0.5px;
    line-height: 1;
  }
  .product-subtitle {
    position: absolute;
    left: 70px;
    top: 160px;
    font-size: 24px;
    font-weight: 400;
    line-height: 1.3;
  }
  .product-note {
    position: absolute;
    left: 524px;
    top: 80px;
    font-size: 14.5px;
    font-weight: 400;
    line-height: 1.2;
  }
  .brand {
    position: absolute;
    left: 56px;
    top: 528px;
    display: flex;
    align-items: center;
    gap: 12px;
  }
  .brand-dot {
    width: 46px;
    height: 46px;
    border-radius: 50%;
    background: var(--yellow);
  }
  .brand-name {
    font-size: 58px;
    font-weight: 800;
    line-height: 1;
    color: var(--navy);
  }
  .geometric-field {
    position: absolute;
    left: 408px;
    top: 262px;
    width: 462px;
    height: 385px;
  }
</style>
</head>
<body>
  <section class="box-front">
    <h1 class="product-title">Medical Kits</h1>
    <p class="product-subtitle">Lorem ipsum dolor<br>sit amet, consec</p>
    <p class="product-note">Lorem ipsum dolor sit<br>amet, consec</p>

    <div class="brand">
      <span class="brand-dot"></span>
      <span class="brand-name">Veltora</span>
    </div>

    <svg class="geometric-field" viewBox="0 0 544 453" role="img"
         aria-label="Geometric pattern of quarter circles and circles in yellow, orange, sky blue and navy">
      <defs>
        <linearGradient id="fieldTone" x1="0" y1="1" x2="1" y2="0">
          <stop offset="0" stop-color="#6aa5c4"/>
          <stop offset="0.35" stop-color="#fcc20a"/>
          <stop offset="0.65" stop-color="#fb9409"/>
          <stop offset="1" stop-color="#121a45"/>
        </linearGradient>
      </defs>
      <polygon fill="url(#fieldTone)"
               points="273,0 544,0 544,453 0,453 0,272 182,272 182,91 273,91"/>
    </svg>
  </section>
</body>
</html>
```